Heron Payments Business card refresh

Need a new design of our business card The info is not what is on these cards i sent this for a reference. I can email all the info over
Info would be Dale Merton Chief HERON is the title. our new address is 47615 Birch Hollow Ln. Alder Springs 93027 Cell number is 805-555-0147 Work number is 855-555-0182 ext 212 Dale@heronpaylane.example is my email address
Target Market(s)
Merchant Services all businesses that take credit cards
Industry/Entity Type
Merchant Services / Credit Card processing
Contact Information for Business Card
Need a new design of our business card The info is not what is on these cards i sent this for a reference. I can email all the info over Info would be Dale Merton Chief HERON is the title. our new address is 47615 Birch Hollow Ln. Alder Springs 93027 Cell number is 805-555-0147 Work number is 855-555-0182 ext 212 Dale@heronpaylane.example is my email address
Requirements
Must have
- My logo and colors from my brand guidelines
Nice to have
- i sent some designs just need a new refresh
Should not have
- nothing specific

```html
<!DOCTYPE html>
<html lang="en">
<head>
<meta charset="utf-8">
<title>Heron Payments Business Card</title>
<link href="https://fonts.googleapis.com/css2?family=Lato:wght@400;700;900&display=swap" rel="stylesheet">
<style>
  :root {
    --backdrop: #2e2e30;
    --card: #23252f;
    --accent: #8dc21f;
    --ink: #ffffff;
  }
  * { margin: 0; padding: 0; box-sizing: border-box; }
  html, body {
    width: 1200px; height: 801px; overflow: hidden;
    background: var(--backdrop);
    font-family: "Lato", Arial, sans-serif;
  }
  .stage {
    position: relative; width: 1200px; height: 801px;
    display: flex; align-items: center; justify-content: center; gap: 50px;
  }
  .card {
    position: relative; width: 525px; height: 300px;
    background: var(--card);
    box-shadow: 0 14px 30px rgba(0,0,0,0.45);
    overflow: hidden;
  }
  /* Front */
  .brand-mark {
    position: absolute; top: 42px; right: 38px;
    display: flex; align-items: center; gap: 10px;
  }
  .brand-mark__square { width: 14px; height: 14px; background: var(--accent); }
  .brand-mark__name {
    color: var(--ink); font-weight: 900; font-size: 24px; letter-spacing: 0.06em;
    white-space: nowrap;
  }
  .divider {
    position: absolute; left: 40px; right: 0; top: 128px;
    height: 1px; background: var(--accent);
  }
  .person { position: absolute; left: 40px; top: 98px; }
  .person__name {
    color: var(--accent); font-weight: 900; font-size: 22px; letter-spacing: 0.02em;
    white-space: nowrap;
  }
  .person__title {
    position: absolute; top: 36px; left: 0; white-space: nowrap;
    color: var(--ink); font-size: 13px;
  }
  .contacts {
    position: absolute; left: 40px; top: 172px; list-style: none;
  }
  .contacts__item {
    display: flex; align-items: center; gap: 9px;
    color: var(--ink); font-size: 12px; line-height: 20px; white-space: nowrap;
  }
  .contacts__icon { width: 11px; height: 11px; fill: var(--accent); flex: none; }
  /* Back */
  .card--back { display: flex; align-items: center; justify-content: center; }
  .brand-mark--large { position: static; gap: 16px; }
  .brand-mark--large .brand-mark__square { width: 26px; height: 26px; }
  .brand-mark--large .brand-mark__name { font-size: 44px; }
</style>
</head>
<body>
<main class="stage">
  <section class="card card--front" aria-label="Business card front">
    <div class="brand-mark">
      <span class="brand-mark__square"></span>
      <span class="brand-mark__name">HERON PAYMENTS</span>
    </div>
    <div class="person">
      <h1 class="person__name">DALE MERTON</h1>
      <p class="person__title">Chief HERON</p>
    </div>
    <div class="divider"></div>
    <ul class="contacts">
      <li class="contacts__item">
        <svg class="contacts__icon" viewBox="0 0 12 12"><path d="M3 0h6a1 1 0 0 1 1 1v10a1 1 0 0 1-1 1H3a1 1 0 0 1-1-1V1a1 1 0 0 1 1-1zm0 1.5v8h6v-8z"/></svg>
        805-555-0147
      </li>
      <li class="contacts__item">
        <svg class="contacts__icon" viewBox="0 0 12 12"><path d="M2.5 0.5l2 2.5-1.2 1.3c.8 1.7 2.2 3.1 3.9 3.9L8.5 7l2.5 2-1 2.3C5 11.5.5 7 .7 1.5z"/></svg>
        855-555-0182
      </li>
      <li class="contacts__item">
        <svg class="contacts__icon" viewBox="0 0 12 12"><path d="M0 2h12v8H0zm1 1l5 4 5-4z"/></svg>
        Dale@heronpaylane.example
      </li>
      <li class="contacts__item">
        <svg class="contacts__icon" viewBox="0 0 12 12"><circle cx="6" cy="6" r="6"/><path d="M1 6h10M6 1v10" stroke="#23252f" stroke-width="1"/></svg>
        www.heronpaylane.example
      </li>
      <li class="contacts__item">
        <svg class="contacts__icon" viewBox="0 0 12 12"><path d="M6 0a4 4 0 0 1 4 4c0 3-4 8-4 8S2 7 2 4a4 4 0 0 1 4-4zm0 2.5a1.5 1.5 0 1 0 0 3 1.5 1.5 0 0 0 0-3z"/></svg>
        47615 Birch Hollow Ln. Alder Springs 93027
      </li>
    </ul>
  </section>
  <section class="card card--back" aria-label="Business card back">
    <div class="brand-mark brand-mark--large">
      <span class="brand-mark__square"></span>
      <span class="brand-mark__name">HERON PAYMENTS</span>
    </div>
  </section>
</main>
</body>
</html>
```